Business Card Update, need to bring life to the card, two sided color

We need a new business card design, are moving and changing addresses and need a new look, we have the logos already attached but need a new style moving forward. Can incorporate the color of the logo (The Green) as well, maybe a solid back? We deal with safety products revolving around static electricity and safety lighting. Would like to keep same font in second logo as well.

Target Market(s)

Electrical Safety, Lighting

Contact Information for Business Card

Lars Whitcombe
Vice President
Office: 555-284-7316
Cell: 555-862-0457
lars@tkwhitcombe.com
www.tkwhitcombe.com
4700 West Cedar Boulevard
Suite #320
Roswell, GA 30412

Font styles to use
Serif
Sans Serif

Requirements
Must have
• Since 1918
Nice to have
• Could use the 100 Year Logo for back of card, would like the back of card to be the same green as logo.
Should not have
• No black cards please.

```html
<!DOCTYPE html>
<html lang="en">
<head>
<meta charset="utf-8">
<title>T.K. Whitcombe – Business Card</title>
<link href="https://fonts.googleapis.com/css2?family=Roboto:wght@400;500;700&display=swap" rel="stylesheet">
<style>
  :root {
    --brand-green: #05985a;
    --paper: #ffffff;
    --ink-grey: #3a3a3a;
    --backdrop: #e4e6e5;
    --on-green: #ffffff;
  }
  * { box-sizing: border-box; margin: 0; padding: 0; }
  html, body { width: 1200px; height: 768px; overflow: hidden; }
  body {
    background: var(--backdrop);
    font-family: "Roboto", Arial, sans-serif;
    position: relative;
  }
  .card {
    position: absolute;
    top: 229px;
    width: 540px;
    height: 310px;
    border-radius: 22px;
    overflow: hidden;
    box-shadow: 0 6px 18px rgba(0,0,0,0.15);
  }
  .card-front { left: 40px; background: var(--paper); }
  .card-back { left: 620px; background: var(--brand-green); color: var(--on-green); }

  /* front */
  .brand {
    position: absolute;
    left: 0; right: 0; top: 88px;
    display: flex; align-items: center; justify-content: center; gap: 16px;
    color: var(--brand-green);
    font-weight: 700;
  }
  .brand-dot {
    width: 70px; height: 70px; border-radius: 50%;
    background: var(--brand-green);
    flex: none;
  }
  .brand-name { font-size: 32px; line-height: 1; letter-spacing: 0.2px; }
  .brand-sub { font-size: 13.5px; margin-top: 4px; letter-spacing: 0.4px; }
  .brand-since { font-size: 11px; margin-top: 4px; letter-spacing: 2px; text-transform: uppercase; font-weight: 500; }
  .front-web {
    position: absolute; left: 0; right: 0; bottom: 42px;
    text-align: center; font-size: 13px; letter-spacing: 5px; color: var(--ink-grey);
  }

  /* back */
  .person { position: absolute; left: 40px; top: 34px; }
  .person-name { font-size: 24px; font-weight: 700; line-height: 1.15; }
  .person-title { font-size: 15px; margin-top: 2px; }
  .address { position: absolute; left: 40px; top: 118px; font-size: 14.5px; line-height: 1.3; }
  .contacts { position: absolute; left: 40px; top: 190px; list-style: none; font-size: 14.5px; }
  .contacts li { display: flex; align-items: center; gap: 8px; height: 19px; white-space: nowrap; }
  .contacts svg { width: 13px; height: 13px; flex: none; }
  .product-art {
    position: absolute; right: 60px; top: 34px;
    width: 92px; height: 244px;
    border-radius: 44px 44px 10px 10px;
    background: rgba(255,255,255,0.92);
  }
</style>
</head>
<body>
  <section class="card card-front">
    <div class="brand">
      <span class="brand-dot"></span>
      <div class="brand-text">
        <div class="brand-name">T.K. Whitcombe</div>
        <div class="brand-sub">Manufacturing Company, Inc.</div>
        <div class="brand-since">Since 1918</div>
      </div>
    </div>
    <div class="front-web">www.tkwhitcombe.com</div>
  </section>

  <section class="card card-back">
    <div class="person">
      <div class="person-name">Lars Whitcombe</div>
      <div class="person-title">Vice President</div>
    </div>
    <div class="address">
      4700 West Cedar Boulevard<br>
      Suite #320<br>
      Roswell, GA 30412
    </div>
    <ul class="contacts">
      <li><svg viewBox="0 0 16 16"><path fill="#fff" d="M3.5 1.5l2.5 0 1 3.5-1.6 1.2a8 8 0 0 0 4.4 4.4L11 9l3.5 1v2.5c0 1-1 2-2 2A11 11 0 0 1 1.5 3.5c0-1 1-2 2-2z"/></svg>555 284 7316</li>
      <li><svg viewBox="0 0 16 16"><rect x="4" y="1" width="8" height="14" rx="1.5" fill="none" stroke="#fff" stroke-width="1.6"/><circle cx="8" cy="12.5" r="0.9" fill="#fff"/></svg>555 862 0457</li>
      <li><svg viewBox="0 0 16 16"><rect x="4" y="1.5" width="8" height="4" fill="#fff"/><rect x="1.5" y="6" width="13" height="6" rx="1" fill="#fff"/><rect x="4" y="11" width="8" height="3.5" fill="#fff" stroke="#05985a" stroke-width="0.8"/></svg>555 390 1186</li>
      <li><svg viewBox="0 0 16 16"><rect x="1.5" y="3.5" width="13" height="9" fill="#fff"/><path d="M1.5 3.5l6.5 5 6.5-5" fill="none" stroke="#05985a" stroke-width="1.2"/></svg>lars@tkwhitcombe.com</li>
      <li><svg viewBox="0 0 16 16"><circle cx="8" cy="8" r="6.5" fill="#fff"/><path d="M1.5 8h13M8 1.5c-3 3.5-3 9.5 0 13M8 1.5c3 3.5 3 9.5 0 13" fill="none" stroke="#05985a" stroke-width="1"/></svg>www.tkwhitcombe.com</li>
    </ul>
    <div class="product-art" role="img" aria-label="White silhouette of a static-safety lamp product"></div>
  </section>
</body>
</html>
```